Personal Business card and maybe logo or graphic?

I would like a card to give out like you would a business card, however I am not promoting a business, it is just for my personal details.

I have no brand and no logo to worry about.

I would like some images or a logo of some kind or a graphic so the card has some excitement about it.

I am happy if you wish to create a logo/graphic that represents my name, I have seen someone with just their initials as a graphic so for me PH, however I am happy for you to create anything you wish, it does not have to relate to me just make the card look fun and still professional.

Please use the details

Peter Hadley

Ashcombe Lodge
9 The Mews
Fern Close
Bournemouth
Dorset
BH4 2QT

+44 (0)7812 604258
peter@hadleypost.example
linkedin.example/in/hadleypeter

looking for a mix between fun, fresh , young whilst being professional

I am new to this and am looking for you to guide me through the process please ask questions and ideas

I am just tidying up my brief as I am starting to understand more. hope it has not confused anyone
Updates

Reason: I have not had time to review or comment due to personal issues sorry

Hi,

to help would you be so kind as to use these sample details on the card

I am uk based and a few designs have us details which look different

Peter Hadley

Ashcombe lodge

9 The Mews

Fern Close

Bournemouth

Dorset

BH4 2QT

+44 (0)7812 604258

peter@hadleypost.example

many thanks hope that is ok and not too much trouble!

regards

Pim

My are of expertise is IT management / IT Consultancy, incase you wish to incorporate any graphics

My job was that of CIO (Chief Information Officer) or another term is Head of IT

just advising incase this gives any assistance as one designer has asked s may be useful to others

thanks                                   

just thought I have had a look and the UK size for a business card seems to be as per below

I thought I would mention as I guess the US size may be different and other countries too

I found these sizes on Cardforge but guess most companies will be similar

that said maybe you can advise me

I have no idea what cardforge is like so not sure where to get cards made, will figure that out later I guess but I assume dimensions are important for the design

thanks

 

Document Trim Size    

            Horizontal        

        85 x 55 mm           

1004 x 650 pixels           

            Vertical        

        55 x 85 mm           

650 x 1004 pixels           

        Full Bleed Size    

            Horizontal        

        88 x 58 mm           

1039 x 685 pixels           

            Vertical        

        58 x 88 mm           

685 x 1039 pixels           

 many thanks

Target Market(s)

Professional and personal contacts

Industry/Entity Type

Business

```html
<!DOCTYPE html>
<html lang="en">
<head>
<meta charset="utf-8">
<title>Peter Hadley – Business Card</title>
<link href="https://fonts.googleapis.com/css2?family=Jura:wght@400;500&display=swap" rel="stylesheet">
<style>
  :root {
    --page: #ffffff;
    --slate: #666666;
    --mint: #00ff99;
    --white: #ffffff;
    --shadow: rgba(0, 0, 0, 0.45);
  }
  * { margin: 0; padding: 0; box-sizing: border-box; }
  html, body {
    width: 954px;
    height: 1200px;
    overflow: hidden;
    background: var(--page);
    font-family: "Jura", sans-serif;
  }
  .canvas { position: relative; width: 954px; height: 1200px; }

  .card {
    position: absolute;
    left: 144px;
    width: 669px;
    height: 418px;
    border-radius: 40px;
    box-shadow: 8px 9px 12px var(--shadow);
    overflow: hidden;
  }
  .card--front { top: 116px; background: var(--slate); --accent: var(--mint); }
  .card--back  { top: 676px; background: var(--mint);  --accent: var(--slate); }

  .card__rule {
    position: absolute;
    left: 0;
    right: 0;
    top: 97px;
    height: 2px;
    background: var(--accent);
  }

  .wordmark {
    position: absolute;
    left: 0;
    right: 0;
    top: 120px;
    text-align: center;
    font-size: 64px;
    font-weight: 400;
    line-height: 1;
    letter-spacing: 2px;
    color: var(--accent);
  }

  .details {
    position: absolute;
    left: 0;
    right: 0;
    text-align: center;
    white-space: nowrap;
  }
  .details--name    { top: 244px; font-size: 21px; font-weight: 500; color: var(--white); }
  .details--address { top: 295px; font-size: 19px; font-weight: 400; color: var(--mint); letter-spacing: 0.5px; }
  .details--contact { top: 329px; font-size: 16px; font-weight: 400; color: var(--mint); word-spacing: 1px; }
  .details--contact .gap { display: inline-block; width: 16px; }
  .details--web     { top: 372px; font-size: 17px; font-weight: 500; color: var(--white); }
</style>
</head>
<body>
<main class="canvas">
  <section class="card card--front" aria-label="Card front">
    <div class="card__rule"></div>
    <div class="wordmark">hadley</div>
    <p class="details details--name">Peter Hadley</p>
    <p class="details details--address">9 THE MEWS&nbsp; BOURNEMOUTH&nbsp; BH4 2QT</p>
    <p class="details details--contact">T&nbsp; 07 812 604 258<span class="gap"></span>E peter@hadleypost.example</p>
    <p class="details details--web">www.hadleypost.example</p>
  </section>

  <section class="card card--back" aria-label="Card back">
    <div class="card__rule"></div>
    <div class="wordmark">hadley</div>
  </section>
</main>
</body>
</html>
```